Yoga Studio needs a new website

I am looking for someone to design a landing/home page for my website. The website will be developed using Wordpress, so please make sure your designs are compatible.

Please note the following design guidelines about the page:
1. The website is for a yoga studio called “Mirel Yoga”. The logo for our studio has been uploaded on along with this project. Mirel in Sanskrit means Truth and Yoga means unity or unification (with supreme consciousness).
2. The Yoga studio will probably the first of its kinda to offer true, authentic, spiritual experience to students in South Africa. More than that, it aims to setup itself as a hub for spiritualists and seekers irrespective of beliefs, religion and what philosophies they subscribe to.
3. Unlike modern schools, this school focuses on true elements of yoga - and teaches Yoga the way it was meant to be - no westernisation. Must have a peaceful, clam, very clean and spiritual look.
4. Please pay careful attention to the logo, color schemes and the simple design. The site must reflect exactly the same principles.
5. Please use the latest web design trends and ideas in your design. You are free to be as creative as you want.
6. You are free to combine or use design concepts from other philosophies such as Sufism, Bahai, Tantra, Buddhism etc. as long as it gels well with the Yoga theme.
7. The overall site should give a very sensual, feminine and very mystic feel.

Functionality, features and guidelines for the main page design:
1. The main page should give a very clean, expansive, clutter free look.
2. The designer should find a clean way to fit all the following links/information into a main page. First prize if the designer could fit everything in a “single screen” - no scrolling.
3. Visually, the following information must be presented on the main page:
1. The name/logo of the studio.
2. The following sections of the website should have a link on the main page. Sub items represent sub sections within a section.
1. Home - Redirects the user back to home page
2. About
1. Mirel Yoga
2. Instructors
3. FAQ
3. Private Sessions
4. Corporate
1. At Workplace
2. Offisite & Team Building
3. Specialized
5. Retreats
6. Therapy
1. Stress & Anxiety
2. Lifestyle Diseases
3. Rehabilitation
4. Others
7. Gallery
8. Contact Us
3. A Calendar for classes and events
4. A section to display latest blog articles with option to share on social media sites.
5. A separate section to display latest news items.
6. A section for photo gallery - the gallery can be categorised in albums. The main page can display a limited number of images and clicking on the image should take user to our flicker account.
7. Lastly, a nice and clean way to show our activity on various social media streams such as facebook, twitter, flickr, Facebook page, google plus etc.

Please do not limit yourself to the brief above. If you any creative ideas or concepts, please feel free to experiment and suggest new features. Use you full creativity.
Updates

Hi, Thank you for all the designs so far and for your hard work. Just wanted to let you know that you can also include design elements from other philosophies as well if you want to such as Sufism, Bahai, Tantra, Buddhism etc. as long as it gels well with the over all Yoga theme. Please also note that the final design have a mystic, feminine and sensual feel to it. Please also try and include/match the logo styles in the design as well. The site should look very premium, very exclusive - just like the logo.

Target Market(s)

the site is being designed for serious yoga practitioners and learners in the age group of 18-45

Industry/Entity Type

School

Requirements
Must have
• clean, expansive, elegant, simple, calming, soothing, peaceful

```html
<!DOCTYPE html>
<html lang="en">
<head>
<meta charset="utf-8">
<title>Mirel Yoga — Home</title>
<link rel="stylesheet" href="https://fonts.googleapis.com/css2?family=Mulish:wght@300;400&family=Arimo:wght@400&family=Tinos:wght@400;700&display=swap">
<style>
  :root {
    --brand-blue: #163f97;
    --brand-blue-text: #1d4aa0;
    --ink: #222222;
    --ink-soft: #333333;
    --nav-grey: #8c8c8c;
    --icon-grey: #5a5a5a;
    --panel-grey: #ebebed;
    --rule-grey: #a9a9ab;
    --divider: #c4c4c6;
    --white: #ffffff;
  }
  * { box-sizing: border-box; margin: 0; padding: 0; }
  html, body { width: 1200px; height: 900px; overflow: hidden; background: var(--white); }
  body { position: relative; font-family: "Arimo", Arial, sans-serif; color: var(--ink); }

  .site-header { position: absolute; left: 0; top: 0; width: 1200px; height: 168px; }
  .brand { position: absolute; left: 0; width: 1200px; top: 62px; text-align: center; }
  .brand-name { font-family: "Mulish", sans-serif; font-weight: 400; font-size: 26px; color: var(--brand-blue); letter-spacing: 1px; display: inline-flex; align-items: center; gap: 10px; }
  .brand-mark { width: 14px; height: 14px; border-radius: 50%; background: var(--brand-blue); }

  .social { position: absolute; display: flex; gap: 6px; }
  .social span { width: 20px; height: 20px; border-radius: 50%; background: var(--icon-grey); display: block; }
  .social--header { left: 1063px; top: 20px; gap: 7px; }

  .main-nav { position: absolute; top: 141px; left: 0; width: 1200px; }
  .main-nav ul { list-style: none; display: flex; }
  .main-nav li { position: absolute; font-family: "Mulish", sans-serif; font-weight: 300; font-size: 14.5px; color: var(--nav-grey); white-space: nowrap; letter-spacing: 0.2px; }
  .main-nav li.is-current { color: var(--ink); font-weight: 400; }

  .hero { position: absolute; top: 168px; left: 0; width: 1200px; height: 375px; }
  .hero-photo { position: absolute; left: 0; top: 0; width: 665px; height: 375px;
    background: linear-gradient(90deg, #6f9a3c 0%, #a6c66c 30%, #c8d9a8 50%, #e9ece6 70%, #f4f4f2 100%); }
  .hero-strip { position: absolute; left: 0; bottom: 0; width: 665px; height: 41px; background: rgba(255,255,255,0.28); }
  .hero-dots { position: absolute; left: 14px; top: 349px; display: flex; gap: 9px; }
  .hero-dots span { width: 15px; height: 15px; border-radius: 50%; background: var(--white); }
  .hero-dots span.is-active { background: var(--brand-blue); }
  .hero-about { position: absolute; left: 665px; top: 0; width: 535px; height: 375px; background: var(--brand-blue); color: var(--white); padding: 50px 46px 0 57px; }
  .hero-about h2 { font-family: "Mulish", sans-serif; font-weight: 300; font-size: 21px; margin-bottom: 22px; }
  .hero-about p { font-size: 13.4px; line-height: 16.8px; }

  .feeds { position: absolute; top: 553px; left: 0; width: 1200px; height: 319px; background: var(--panel-grey); }
  .feed { position: absolute; top: 35px; width: 346px; }
  .feed h3 { font-family: "Mulish", sans-serif; font-weight: 300; font-size: 22px; color: #444; padding-left: 3px; height: 31px; border-bottom: 6px solid var(--rule-grey); }
  .feed--blog { left: 37px; }
  .feed--news { left: 426px; }
  .feed--calendar { left: 812px; }
  .feed-divider { position: absolute; top: 35px; width: 1px; height: 250px; background: var(--divider); }

  .post { position: absolute; font-size: 12px; line-height: 14px; color: var(--ink-soft); }
  .post::before { content: ""; position: absolute; left: -17px; top: 4px; width: 5px; height: 5px; border-radius: 50%; background: var(--ink); }
  .post-title { color: var(--ink); text-decoration: underline; text-decoration-color: #888; display: block; }
  .post-date { display: block; }
  .feed--blog .post-date { color: var(--brand-blue-text); }
  .feed--news .post-date { color: var(--ink); }
  .post .social { position: static; margin: 14px 0 0 -5px; gap: 4px; }

  .calendar { position: absolute; left: 55px; top: 58px; width: 240px; border-collapse: collapse; background: var(--white); font-family: "Tinos", serif; }
  .calendar caption { background: var(--white); font-size: 10px; font-weight: 700; border: 1px solid #bbb; border-bottom: none; height: 14px; line-height: 14px; }
  .calendar th { font-size: 5px; font-weight: 400; border: 1px solid #bbb; height: 9px; text-transform: uppercase; }
  .calendar td { border: 1px solid #bbb; height: 31px; width: 34px; text-align: center; font-size: 13px; font-weight: 700; }

  .site-footer { position: absolute; left: 0; top: 872px; width: 1200px; height: 28px; background: var(--brand-blue); }
</style>
</head>
<body>
  <header class="site-header">
    <div class="brand"><span class="brand-name"><span class="brand-mark"></span>Mirel Yoga</span></div>
    <div class="social social--header" aria-label="Social links"><span></span><span></span><span></span><span></span></div>
    <nav class="main-nav">
      <ul>
        <li class="is-current" style="left:89px">HOME</li>
        <li style="left:194px">ABOUT</li>
        <li style="left:304px">PRIVATE SESSIONS</li>
        <li style="left:499px">CORPORATE</li>
        <li style="left:647px">RETREATS</li>
        <li style="left:779px">THERAPY</li>
        <li style="left:904px">GALLERY</li>
        <li style="left:1027px">CONTACT US</li>
      </ul>
    </nav>
  </header>

  <section class="hero">
    <div class="hero-photo" role="img" aria-label="Photo of a woman in white meditating cross-legged on green grass"></div>
    <div class="hero-strip"></div>
    <div class="hero-dots"><span class="is-active"></span><span></span><span></span><span></span></div>
    <div class="hero-about">
      <h2>About us</h2>
      <p>The website is for a yoga studio called “Mirel Yoga”. The logo for our studio has been uploaded on along with this project. Mirel in Sanskrit means Truth and Yoga means unity or unification (with supreme consciousness).<br>
      2. The Yoga studio will probably the first of its kinda to offer true, authentic, spiritual experience to students in South Africa. More than that, it aims to setup itself as a hub for spiritualists and seekers irrespective of beliefs, religion and what philosophies they subscribe to.<br>
      3. Unlike modern schools, this school focuses on true elements of yoga - and teaches Yoga the way it was meant to be - no westernisation. Must have a peaceful, clam, very clean and spiritual look.</p>
    </div>
  </section>

  <section class="feeds">
    <div class="feed feed--blog">
      <h3>latest blog</h3>
    </div>
    <div class="post" style="left:59px;top:98px;width:320px">
      <span class="post-title">Money and love: The politics of competitive matrimony isn't confined to UP awards for inter-caste marriage</span>
      <span class="post-date">February 2, 2015, 12:08 AM IST</span>
      With the dust having yet to settle on the contentious issue of so-called ‘love jihad’...
      <div class="social"><span></span><span></span><span></span><span></span></div>
    </div>
    <div class="post" style="left:56px;top:218px;width:320px">
      <span class="post-title">Money and love: The politics of competitive matrimony isn't confined</span>
      <span class="post-date">February 2, 2015, 12:08 AM IST</span>
      With the dust having yet to settle on the contentious issue of so-called ‘love jihad’...
      <div class="social" style="margin-top:12px"><span></span><span></span><span></span><span></span></div>
    </div>

    <div class="feed-divider" style="left:404px"></div>

    <div class="feed feed--news">
      <h3>latest news</h3>
    </div>
    <div class="post" style="left:463px;top:97px;width:310px">
      <span class="post-title">Money and love: The politics of competitive matrimony isn't confined to UP awards for inter-caste marriage</span>
      <span class="post-date">February 2, 2015, 12:08 AM IST</span>
      With the dust having yet to settle on the contentious issue of so-called ‘love jihad’...
    </div>
    <div class="post" style="left:467px;top:207px;width:310px">
      <span class="post-title">Money and love: The politics of competitive matrimony isn't confined to UP awards for inter-caste marriage</span>
      <span class="post-date">February 2, 2015, 12:08 AM IST</span>
      With the dust having yet to settle on the contentious issue of so-called ‘love jihad’...
    </div>

    <div class="feed-divider" style="left:790px"></div>

    <div class="feed feed--calendar">
      <h3>Calendar</h3>
      <table class="calendar">
        <caption>2015 JANUARY</caption>
        <tr><th>Sunday</th><th>Monday</th><th>Tuesday</th><th>Wednesday</th><th>Thursday</th><th>Friday</th><th>Saturday</th></tr>
        <tr><td></td><td></td><td></td><td></td><td>1</td><td>2</td><td>3</td></tr>
        <tr><td>4</td><td>5</td><td>6</td><td>7</td><td>8</td><td>9</td><td>10</td></tr>
        <tr><td>11</td><td>12</td><td>13</td><td>14</td><td>15</td><td>16</td><td>17</td></tr>
        <tr><td>18</td><td>19</td><td>20</td><td>21</td><td>22</td><td>23</td><td>24</td></tr>
        <tr><td>25</td><td>26</td><td>27</td><td>28</td><td>29</td><td>30</td><td>31</td></tr>
      </table>
    </div>
  </section>

  <footer class="site-footer"></footer>
</body>
</html>
```